Beachfront Boutique Hotel Web Design
Pelora Sands Belize Hotel Website Design
Beachfront Boutique Hotel Web Design - Hospitality Industry
Creative Brief
Hospitality Industry
Pelora Sands is located only fifty feet or so from the breathtaking Caribbean Sea on the tranquil island of Caye Caulker Belize with individual one-bedroom suites tastefully decorated to blend in with the island atmosphere. Each fully air-conditioned unit features either a king-sized bed or 2 queen-sized beds, private bath hot/cold water living room area cable flat screen TV, kitchenette and each has its own spacious deck space. Our ultra spacious units each with a approx. 500 sq ft of inside space makes them the most spacious yet affordable vacation units on the island. Warm furnishings make them a home away from home. This is the premier property on Caye Caulker. Come enjoy our breezy verandahs and starlit nights in relaxed comfort. Welcome to a beautiful island escape. These are beachfront condos that are among the best on the island. Step out from your deck and walk on the beach!
Like... Fun, whimsical, relaxing, chillax, simple, colorful, beachy, funky, flash, eye-catching, unique Dislike... Dull, difficult, complicated, busy, plain, standard, boring, blah
Fun
Teal, hot pink, orange, lime green, yellow, blue
https://photoshare.example-albums.com/582093746105829374610/PeloraSands?authkey=Tq8zLmWpR3vXnB7yH2dKcE
sociallink.example.com/PeloraSands
brindlecoveretreat.com
Link 1 is Fotalo album with logo, artwork and possible mock up. Link 2 is the Chatterly page for the hotel Link 3 is a website I like the general look of. Need the following headings: Beachfront Suites Rates & Reservations Gallery All About Caye Caulker Contact Us Need links to CH, Quipster and RoamRater widget. Would like flash... possible changing wallpaper (beach theme) and moving/flash heading/link/buttons :)

```html
<!DOCTYPE html>
<html lang="en">
<head>
<meta charset="utf-8">
<title>Pelora Sands Suites – Gallery</title>
<link rel="stylesheet" href="https://fonts.googleapis.com/css2?family=Open+Sans:wght@400;600;700&display=swap">
<style>
  :root {
    --sky-top: #1f5fa8;
    --sky-mid: #5fa6d6;
    --sea: #3cc0c8;
    --sand: #e9e2cf;
    --orange: #f47a1f;
    --orange-dark: #e0600f;
    --teal-panel: rgba(52, 196, 208, 0.82);
    --white: #ffffff;
    --blue-btn: #2f6fb7;
    --thumb-1: #d7567a;
    --thumb-2: #c9773e;
    --thumb-3: #6fb7a4;
    --thumb-4: #4e9c8f;
  }
  * { box-sizing: border-box; margin: 0; padding: 0; }
  html, body { width: 1200px; height: 821px; overflow: hidden; }
  body { font-family: "Open Sans", Arial, sans-serif; color: var(--white); }

  .page { position: relative; width: 1200px; height: 821px; overflow: hidden; }

  .page-backdrop {
    position: absolute; inset: 0;
    background: linear-gradient(180deg, var(--sky-top) 0%, var(--sky-mid) 38%, #8fd0e6 55%, var(--sea) 66%, #bfe3dc 76%, var(--sand) 88%);
  }

  .brand {
    position: absolute; left: 112px; top: 96px; width: 215px;
    font-size: 30px; font-weight: 700; line-height: 1.1; text-align: center; color: var(--white);
  }

  .search {
    position: absolute; left: 881px; top: 62px; display: flex; height: 24px;
  }
  .search-field {
    width: 136px; background: var(--white); border-radius: 3px 0 0 3px;
    color: #777; font-size: 11px; padding: 4px 8px;
  }
  .search-button {
    width: 24px; background: var(--blue-btn); border-radius: 0 3px 3px 0;
    display: flex; align-items: center; justify-content: center;
  }

  .social {
    position: absolute; left: 940px; top: 104px; display: flex; gap: 8px;
  }
  .social-link {
    width: 32px; height: 32px; border-radius: 50%; background: var(--blue-btn);
    font-size: 10px; font-weight: 700; display: flex; align-items: center; justify-content: center;
    color: var(--white); text-decoration: none;
  }

  .main-nav {
    position: absolute; left: 427px; top: 163px; width: 622px; height: 39px;
    background: var(--orange); border-bottom: 3px solid var(--orange-dark);
    display: flex; align-items: center; justify-content: space-around; padding: 0 8px;
  }
  .main-nav a {
    color: var(--white); text-decoration: none; font-size: 12px; font-weight: 600;
    text-transform: uppercase; white-space: nowrap;
  }
  .main-nav a.is-current { border-bottom: 2px solid var(--white); padding-bottom: 2px; }

  .content-panel {
    position: absolute; left: 113px; top: 310px; width: 955px; height: 352px;
    background: var(--teal-panel); border-radius: 12px; padding: 26px 42px;
  }
  .content-title { font-size: 22px; font-weight: 700; letter-spacing: 0.5px; margin-bottom: 10px; }
  .gallery-row { display: flex; gap: 43px; margin-bottom: 16px; }
  .gallery-thumb {
    width: 170px; height: 91px; border: 3px solid var(--white); border-radius: 3px;
  }
  .gallery-thumb.t1 { background: linear-gradient(160deg, #7fc4e8, var(--thumb-1) 60%, #3b8f4b); }
  .gallery-thumb.t2 { background: linear-gradient(160deg, #e7b174, var(--thumb-2) 70%); }
  .gallery-thumb.t3 { background: linear-gradient(160deg, #f2efe6, var(--thumb-3) 70%); }
  .gallery-thumb.t4 { background: linear-gradient(160deg, #d8ebe3, var(--thumb-4) 70%); }
  .content-text { font-size: 12.4px; line-height: 1.5; margin-bottom: 14px; }

  .site-footer {
    position: absolute; left: 0; top: 732px; width: 1200px; height: 89px;
    background: var(--orange); text-align: center;
  }
  .footer-nav { display: flex; justify-content: center; gap: 22px; margin-top: 36px; }
  .footer-nav a { color: var(--white); text-decoration: none; font-size: 11px; font-weight: 600; text-transform: uppercase; }
  .copyright { font-size: 9px; margin-top: 8px; color: #ffe6cf; }
  .footer-brand {
    position: absolute; right: 120px; top: 24px; width: 140px;
    font-size: 16px; font-weight: 700; line-height: 1.15; color: var(--white); text-align: center;
  }
</style>
</head>
<body>
<div class="page">
  <div class="page-backdrop" role="img" aria-label="Photo of a palm-lined Caribbean beach with boats on white sand under a blue sky"></div>

  <header>
    <div class="brand">Pelora Sands Suites</div>

    <div class="search">
      <div class="search-field">Search</div>
      <div class="search-button">
        <svg width="12" height="12" viewBox="0 0 12 12"><circle cx="5" cy="5" r="3.5" fill="none" stroke="#fff" stroke-width="1.6"/><line x1="7.6" y1="7.6" x2="11" y2="11" stroke="#fff" stroke-width="1.8"/></svg>
      </div>
    </div>

    <nav class="social" aria-label="Social links">
      <a class="social-link" href="#">CH</a>
      <a class="social-link" href="#">Q</a>
      <a class="social-link" href="#">
        <svg width="16" height="12" viewBox="0 0 16 12"><rect x="1" y="1" width="14" height="10" fill="none" stroke="#fff" stroke-width="1.5"/><polyline points="1,1 8,7 15,1" fill="none" stroke="#fff" stroke-width="1.5"/></svg>
      </a>
    </nav>

    <nav class="main-nav" aria-label="Main">
      <a href="#">Beach Suits</a>
      <a href="#">Rates &amp; Reservation</a>
      <a href="#" class="is-current">Gallery</a>
      <a href="#">All About Caye</a>
      <a href="#">Caulker</a>
      <a href="#">Contact Us</a>
    </nav>
  </header>

  <main class="content-panel">
    <h1 class="content-title">GALLERY</h1>
    <div class="gallery-row">
      <div class="gallery-thumb t1" role="img" aria-label="Colourful beach cottage with palm trees"></div>
      <div class="gallery-thumb t2" role="img" aria-label="Suite bedroom with warm furnishings"></div>
      <div class="gallery-thumb t3" role="img" aria-label="Bright living room with sofa"></div>
      <div class="gallery-thumb t4" role="img" aria-label="Kitchenette and dining area"></div>
    </div>
    <p class="content-text">Pelora Sands is located only fifty feet or so from the breathtaking Caribbean Sea on the tranquil island of Caye Caulker Belize are individual one-bedroom suites tastefully decorated to blend in with the island atmosphere. Each fully air conditioned unit features either a king-sized bed or 2 queen-sized beds, private bath hot/cold water living room area cable flat screen TV, kitchenette and each has its own spacious deck space.</p>
    <p class="content-text">Our ultra spacious units each with a approx. 500 sq ft of inside space makes them the most spacious yet affordable vacation units on the island. Warm furnishings make them a home away from home. This is the premier property on Caye Caulker. Come enjoy our breezy verandahs and starlit nights in relaxed comfort. Welcome to a beautiful island escape. These are beachfront condos that are among the best on the island. Step out from your deck and walk on the beach!</p>
  </main>

  <footer class="site-footer">
    <nav class="footer-nav" aria-label="Footer">
      <a href="#">Beach Suits</a>
      <a href="#">Rates &amp; Reservation</a>
      <a href="#">Gallery</a>
      <a href="#">All About Caye</a>
      <a href="#">Caulker</a>
      <a href="#">Contact Us</a>
    </nav>
    <p class="copyright">COPYRIGHT 2011, ALL WEBDESIGN RIGHTS RESERVED</p>
    <div class="footer-brand">Pelora Sands Suites</div>
  </footer>
</div>
</body>
</html>
```